Evaporative Air Conditioning Summer Service

Would like to design a flyer to send out in an email to existing clients to promote a Pre-summer service for Evaporative Air Conditioners
Cost will be $110.00 inc gst
Tasks included in service are
- Inspection and clean of pads
- Inspection and check float valve, water pump, fan, motor, bearings, drain
- Clean basin
- Supply of bacterial tablet
- Inspect overall condition of unit
- Any repairs if required will be quoted
Please see files attached of a previous very basic flyer I have used for installation and replacement unit costs. This has current contact information
Have also uploaded company logo for use.
Thanks

```html
<!DOCTYPE html>
<html lang="en">
<head>
<meta charset="utf-8">
<title>Pre-Summer Service Flyer</title>
<link rel="stylesheet" href="https://fonts.googleapis.com/css2?family=Oswald:wght@600&family=Exo+2:ital,wght@0,600;1,300&family=Roboto:wght@400;500&display=swap">
<style>
  :root {
    --backdrop: #e6e7e9;
    --paper: #ffffff;
    --brand-blue: #1170b8;
    --deep-blue: #1d4fa0;
    --brand-orange: #f28c28;
    --gold: #f7b21c;
    --silver: #b9bcc0;
    --ink: #1c1c1c;
  }
  * { margin: 0; padding: 0; box-sizing: border-box; }
  html, body { width: 1200px; height: 1200px; overflow: hidden; background: var(--backdrop); }
  .flyer {
    position: absolute; left: 200px; top: 35px; width: 800px; height: 1130px;
    background: var(--paper); overflow: hidden;
    box-shadow: 0 6px 24px rgba(0,0,0,.18);
  }
  .brand {
    position: absolute; left: 52px; top: 62px;
    display: flex; align-items: center; gap: 12px;
    font-family: "Exo 2", sans-serif; font-weight: 600; font-size: 30px;
    color: var(--brand-blue); letter-spacing: .5px;
  }
  .brand-dot { width: 40px; height: 40px; border-radius: 50%; background: var(--brand-orange); }
  .hero { position: absolute; left: 0; top: 100px; width: 800px; height: 460px; }
  .headline {
    position: absolute; left: 58px; top: 560px; width: 690px;
    font-family: "Oswald", sans-serif; font-weight: 600; font-size: 78px; line-height: 1;
    color: var(--brand-blue); letter-spacing: -1px; white-space: nowrap;
  }
  .subhead {
    position: absolute; left: 55px; top: 644px;
    font-family: "Exo 2", sans-serif; font-weight: 600; font-size: 40px; line-height: 1;
    color: var(--brand-orange); white-space: nowrap;
  }
  .subhead em { font-weight: 300; font-style: italic; }
  .technician-photo {
    position: absolute; left: 0; top: 777px; width: 350px; height: 353px;
    background: linear-gradient(160deg, #f2f3f5 0%, #dde1e6 45%, #2f6fb7 90%);
    -webkit-mask-image: linear-gradient(90deg, #000 70%, transparent 100%);
            mask-image: linear-gradient(90deg, #000 70%, transparent 100%);
  }
  .price-badge {
    position: absolute; left: 93px; top: 702px; width: 220px; height: 220px; border-radius: 50%;
    background: radial-gradient(circle at 35% 25%, #6f9bd6 0%, #2e66b5 45%, var(--deep-blue) 100%);
    border: 2px solid #fff;
    display: flex; flex-direction: column; align-items: center; justify-content: center;
    font-family: "Oswald", sans-serif; font-weight: 600; color: #fff; line-height: 1.05;
  }
  .price-amount { font-size: 54px; }
  .price-note { font-size: 42px; }
  .includes-tag {
    position: absolute; left: 373px; top: 724px; width: 168px; height: 38px; border-radius: 12px;
    background: linear-gradient(180deg, #3b8fd6, var(--deep-blue));
    color: #fff; font-family: "Roboto", sans-serif; font-weight: 500; font-size: 25px;
    display: flex; align-items: center; justify-content: center;
  }
  .service-list {
    position: absolute; left: 380px; top: 770px; list-style: none;
    font-family: "Roboto", sans-serif; font-size: 17px; line-height: 23px; color: var(--ink);
  }
  .service-list li { position: relative; padding-left: 20px; }
  .service-list svg { position: absolute; left: 0; top: 5px; width: 14px; height: 14px; }
  .contact { position: absolute; left: 340px; top: 968px; width: 400px; text-align: center; }
  .call-line { font-family: "Exo 2", sans-serif; font-weight: 600; font-size: 32px; color: var(--brand-orange); line-height: 1.1; }
  .call-line span { font-weight: 300; }
  .phone { font-family: "Exo 2", sans-serif; font-weight: 600; font-size: 58px; color: var(--brand-blue); line-height: 1.05; letter-spacing: 1px; }
  .email { font-family: "Roboto", sans-serif; font-size: 17px; color: var(--ink); margin-top: 2px; }
  .abn { font-family: "Roboto", sans-serif; font-size: 17px; color: var(--brand-orange); margin-top: 12px; }
  .abn strong { font-weight: 500; }
</style>
</head>
<body>
<main class="flyer">
  <div class="brand"><span class="brand-dot"></span>Keystone Gas &amp; Plumbing</div>

  <svg class="hero" viewBox="0 0 800 460">
    <defs>
      <clipPath id="hero-clip">
        <path d="M0 90 C60 130 140 150 230 125 C400 80 560 -5 700 2 C760 5 790 15 800 25 L800 330 C760 300 680 285 580 295 C400 320 200 460 0 400 Z"/>
      </clipPath>
      <linearGradient id="hero-fill" x1="0" y1="0" x2="1" y2="0">
        <stop offset="0" stop-color="#a9bcc6"/>
        <stop offset=".5" stop-color="#d9e1e6"/>
        <stop offset="1" stop-color="#6f9a6a"/>
      </linearGradient>
    </defs>
    <rect role="img" aria-label="Photo of outdoor air conditioning units beside a stone wall" width="800" height="460" fill="url(#hero-fill)" clip-path="url(#hero-clip)"/>
    <path d="M0 90 C60 130 140 150 230 125" fill="none" stroke="var(--brand-orange)" stroke-width="10"/>
    <path d="M0 100 C60 140 140 160 230 135" fill="none" stroke="var(--silver)" stroke-width="6"/>
    <path d="M230 125 C400 80 560 -5 700 2 C760 5 790 15 800 25" fill="none" stroke="var(--deep-blue)" stroke-width="9"/>
    <path d="M300 118 C450 70 580 10 700 14 C760 17 790 25 800 32" fill="none" stroke="var(--gold)" stroke-width="5"/>
    <path d="M800 330 C760 300 680 285 580 295 C400 320 200 460 0 400" fill="none" stroke="var(--silver)" stroke-width="6"/>
    <path d="M800 340 C760 312 680 298 580 306 C400 330 210 470 0 412" fill="none" stroke="var(--gold)" stroke-width="9"/>
    <path d="M800 352 C760 325 680 312 580 320 C400 345 220 485 0 428" fill="none" stroke="var(--deep-blue)" stroke-width="12"/>
  </svg>

  <h1 class="headline">PRE-SUMMER SERVICE</h1>
  <p class="subhead"><em>for</em> Evaporative Air Conditioners</p>

  <div class="technician-photo" role="img" aria-label="Photo of a technician servicing a wall-mounted air conditioner"></div>

  <div class="price-badge">
    <span class="price-amount">$110.00</span>
    <span class="price-note">inc GST</span>
  </div>

  <div class="includes-tag">INCLUDES:</div>
  <ul class="service-list">
    <li><svg viewBox="0 0 14 14"><circle cx="7" cy="7" r="7" fill="var(--brand-orange)"/><path d="M3.8 7.2 6 9.3 10.2 4.9" fill="none" stroke="#fff" stroke-width="1.8"/></svg>Inspection &amp; clean of pads</li>
    <li><svg viewBox="0 0 14 14"><circle cx="7" cy="7" r="7" fill="var(--brand-orange)"/><path d="M3.8 7.2 6 9.3 10.2 4.9" fill="none" stroke="#fff" stroke-width="1.8"/></svg>Inspection &amp; check float valve,<br>water pump, fan, motor, bearings, drain</li>
    <li><svg viewBox="0 0 14 14"><circle cx="7" cy="7" r="7" fill="var(--brand-orange)"/><path d="M3.8 7.2 6 9.3 10.2 4.9" fill="none" stroke="#fff" stroke-width="1.8"/></svg>Clean basin</li>
    <li><svg viewBox="0 0 14 14"><circle cx="7" cy="7" r="7" fill="var(--brand-orange)"/><path d="M3.8 7.2 6 9.3 10.2 4.9" fill="none" stroke="#fff" stroke-width="1.8"/></svg>Supply of bacterial tablet</li>
    <li><svg viewBox="0 0 14 14"><circle cx="7" cy="7" r="7" fill="var(--brand-orange)"/><path d="M3.8 7.2 6 9.3 10.2 4.9" fill="none" stroke="#fff" stroke-width="1.8"/></svg>Inspect overall condition of unit</li>
    <li><svg viewBox="0 0 14 14"><circle cx="7" cy="7" r="7" fill="var(--brand-orange)"/><path d="M3.8 7.2 6 9.3 10.2 4.9" fill="none" stroke="#fff" stroke-width="1.8"/></svg>Any repairs if required will be quoted</li>
  </ul>

  <div class="contact">
    <p class="call-line">CALL US <span>TODAY</span></p>
    <p class="phone">0455123987</p>
    <p class="email">admin@keystonegasandplumbing.com.au</p>
    <p class="abn">ABN <strong>48019236557</strong></p>
  </div>
</main>
</body>
</html>
```